New website for Scuba Diving School ‘ReefLark’ in Dublin, Ireland

New website for Scuba Diving School ‘ReefLark’ based in Dublin, Ireland.

GENERAL DESCRIPTION OF WHAT I WANT THIS WEBSITE TO BE:

Website must be professional and modern looking. It has to be user friendly so that everybody can easily find information they are looking for. I would like to see the site being innovative and funky yet still appeal to the main market which is 25-35 years old with 2/3 being male middle to high income.

Site should be creative with bright colours. As the site is for scuba diving school it should be cheerful and welcoming. Colours should be eye catching and worm to create friendly image from a very first time it’s visited. Images used in the website should stay as realistic as possible yet professional.

Home Page:
Section 1) Left up to you if you want anything above the menu bar.

Section 2) Under need I want to have menu bar that will have 6 main pages and 6 subpages. How you designed the menu bar is up to you as long as you stick the correct content:

Main Page 1. Home
Main Page 2. About Us
Main Page 3. Courses & Prices
Sub Page - Try a Dive Evening
Sub Page - Scuba Review
Sub Page - Beginners Course
Sub Page - Advanced Open water
Sub Page - Rescue Diver
Sub Page - DiveMaster Course
Main Page 4. Contact Us
Main Page 5. FAQ
Main Page 6. Calendar

Section 3)
I would like to stick to minimum text content on the main page but I would like to see the following:

Under the menu bar please create an image slide show that will change every couple of seconds or can be operated by user when clicked on dot, number or arrow. Example can be found on the fallowing website: http://www.veltrino.example/?tv or http://www.marovent.example/dive/ this is just to give you an idea. I want this slide show to be creative and promote all courses one by one. Pictures in the slide show must be relevant and professional. On each slide please use exact content provided below:

- 1st slide. Content: "Try a Dive Evening for ONLY 49€'
- 2nd slide Content: “Sign up Today for your Beginners Course"
- 3rd slide Content: "Merv Advanced Diver Course"
- 4th slide Content: "The Merv Rescue Diver Course"
- 5th slide Content: "ClipCam with Merv DiveMaster course"

Please link those slides with appropriate course pages so the user can be redirected directly to the course page.

Section 4)
On the bottom of the page I would like to see all links in columns in small print with my logo in the right bottom corner. Please make the logo clearly visible

ADDITIONAL INFORMATION:

Also, somewhere on the page I would like to see some form of a price tag that will attract user attention. The purpose of this price tag is for the user to click on it to check our discounts.

Content for the Price Tag: “MATES RATES 10%OFF” and when clicked it will bring up a pop up window that will state the following:
POP UP Content:

“Sign up now for our next "Try a Dive Evening" and get 10% when you come with your friend! Bring two friends and get 10% off of your next Beginners course"!
Contact us now to book your place!

‘Contact us’ should be a link that will redirect user to the ‘Contact Us’ Page. (This should be done on all pages) plus the link to the calendar page.

About us Page:

Section 1 and Section 2 from the home page should be repeated.

Section 3) Content:

This section will be information to give a customer overview of who we are and what we do. I will provide you with the picture in the next 3-4 day (waiting for the photographer to get back to me) which I would like to be included on this page with fallowing information: Tomas Rellick Merv No. 574830.
Also I would like this picture to be part of the fallowing content:
Please stick to exact wording:

Content:
Welcome to ReefLark

We are Dublin based scuba diving school dedicated to teaching Scuba Diving in the internationally recognised MERV diving system. We have a real passion for diving and love everything about the real magic that the underwater world has to offer.

We teach a range of courses starting from a very beginning right through to professional level diving. All our staffs are official Scuba Diving MERV, KLT instructors and MERV DiveMasters.

We take great pride in our professional approach to diving and can guarantee that that you will receive the highest level of expertise and attention available whether you are trying just one evening of scuba or completing your Dive Master program.

ReefLark is a progressive Eco minded business promoting safe and responsible diving. In everything we do. Everybody who learns to scuba dive with us is taught that safety is at the heart of everything we do in Scuba. The whole worlds of the oceans are opened up to be discovered. We believe that we can all make a huge difference in keeping our oceans healthy and self-sustaining for the generations to come.

Meet our owner and MERV qualified Instructor at ReefLark.

“I am originally from Poland but moved to Ireland in 2006 and yes I have a Dublin accent now! When I started my adventures in diving here was keen to explore the wonders of many of great diving sites in Irelands surrounding coastline. I am a professionally qualified Merv Open Water Instructor and I really enjoy working with students on all levels. I have a genuine love and passion for the Irish waters and from the beginning when I sold my car to purchase my first diving equipment I knew this is the path in life that I want to take. I LOVE THE WATER! Most people probably don’t know that Ireland is one of the best places in the world for scuba diving. The diversity of marine life on Ireland’s coasts is absolutely fantastic. Now that we have a great Harbourview Swim Arena we have unrivalled facilities for people to start with scuba in the controlled surroundings before moving on to discover the great underwater world in the seas. I encourage everybody to give it a go and discover for themselves what turned my world upside down”.

Section 4)

Courses Page

Section 1 and Section 2 from the home page should be repeated on each course page. I don’t want all courses on one page that’s why I listed them as subpages in form of a dropdown menu. I want the customer to have a choice where they go so they can skip the information that is not relevant to them.

Please stick to the exact content provided below. Please use some images on each of the course pages to reflect the information provided for the customer. Again please make the images smaller so they add to the page and not still attention from the text.

Furthermore, please call each page in the drop down menu as you can see them in Section 2 of the home page.

• Subpage 1 ‘Try a Dive’
Content:
Discover Scuba Diving (Price Tag: Only 49€)
Have you ever seen those underwater documentaries and wish you could discover the amazing world of scuba for yourself? Or have you ever watched a scuba diver on TV and wondered if you could ever experience the fascinating world that exists under the sea? Or did you know Ireland has some of the most fascinating and diverse marine ecosystems in the world and they are right on our door step? Well now you can easily discover scuba for yourself in the comfort of the world class facilities at Dublin’s Harbourview Swim Arena under the direction and supervision of a ReefLark Scuba Instructor.

This Discover Scuba Diving Merv program is a great introduction to the magical world of scuba. In the comfort of the swimming pool under watchful eye of your instructor you will get a chance to learn a few basics about scuba diving, practice some fun skills and familiarise yourself with scuba equipment

There is no need for previous experience or the ability to swim like an Olympian. You just need a towel and a swimsuit and we provide you with the rest.
Our Discover Scuba Diving night happens on Tuesday evenings 7-10pm using the facilities at the Harbourview Swim Arena.

It really is that simple so don’t wait any longer!

Contact us today to book your adventure now.

• Subpage 2 ‘Scuba Review’
Content:
Scuba Review (Price Tag: Only 59€)
If it been a while since you had a chance to dive with your buddy and your skills are a bit rusty or maybe you thinking of doing some scuba again on holiday then why not take part in this scuba review program to refresh your skills at the Harbourview Swim Arena

Merv Scuba Review was designed for anybody who is certified but has stopped diving for a while and would like to get back into the sport again .During this one- evening session our instructor will review your diving knowledge and help you practice your skills before you head back to the open water.

There is no requirement to take the full theory test again.

Simply contact us to complete your Scuba Review!

• Subpage 3 ‘Beginners Course’
Content:
Open Water Diver (Price Tag: Only 559€)
The MERV Open Water course opens the door of a whole new world of discovery. Everything that happens underwater from discovering our amazing diverse marine life to diving to see long lost ship wrecks all begins with completing your first Open Water course. Once you have completed this course you will be awarded your own internationally recognized scuba diving license which allows you to explore the wonderful world of scuba on any future holidays or international travels.

If you've always wanted to learn how to scuba dive, this course is the best way to start. The MERV Open Water Diver course is the world's most popular scuba course, and has introduced millions of people to the adventurous diving lifestyle.

Breathing under water for the first time is something new and unforgettable. Our Merv Open Water course is structured in a way that allows you to study at your own comfortable pace. The course teaches you the scuba diving theory behind diving, and allows you to practice your diving skills in the comfort of the swimming pool in the world class facility of the Harbourview Swim Arena. We will then take you out into the sea for your open water dives to allow you practice your new scuba diving skills under our professional supervision.

We designed our courses to fit your busy life style. Our classroom and pool training takes place every Tuesday in Harbourview Swim Arena from 7 to 10 pm. Once you have enough knowledge of the scuba diving basics completed in the pool we will then take you diving in the open water at one of the great local dive sites. We offer a high degree of flexibility to people completing the course and if you do miss some classes we schedule extra time at no extra cost to allow your course completion.

Our course runs over a period of six weeks. Five evening’s sessions in the pool and one weekend at one of our regular dive sites.

What you need is a towel and a swimsuit the rest will be provided.
You can start your Open Water Diver course today by simply getting in touch with us by clicking on Contact us.

• Subpage 4 ‘Advanced Open water’
Content:
Advanced Open Water Diver (Price Tag: Only 389€)

Keeping your diving skills sharp is an important part of scuba diving. Once you have completed your Open Water scuba course and begin to feel comfortable with your dives then you may decide you wish to learn additional diving skills, undertake some deeper dives and further develop your knowledge of scuba diving. Our Advance Open Water Course is specially designed for this purpose.

This course is structured in a way that enables you to learn more about the various different types of diving. It includes 5 great adventure dives that will allow you maximize the enjoyment of your diving skills and as safety is always our priority the course is completed under the guidance of our experienced qualified ReefLark instructor.
This course involves some theory without the need for final exam so you will have more time to enjoy some of our awesome dive sites.

This course is only suitable if you have already completed your MERV Open Water Diver (or qualifying certification from another training organization). But remember You don't need to have your own diving equipment as ReefLark will provide everything you need for course participation.

The course is conducted over one weekend and we run advanced courses regularly all year round. If you can't make it on the weekends we can also run it during the week.
You can start your Advanced Open Water Diver course today by simply getting in touch with us by clicking on Contact us.

• Subpage 5 ‘Rescue Diver’
Content:
Rescue Diver (Price Tag: Only 369€)

Scuba diving is one of the most enjoyable and fulfilling activities experienced by thousands of people around the world every day. The popularity of recreational diving continues to increase every year. The diving community places safety as our number one primary concern for all participants in the sport.

The Merv Recue Diver program is designed to teach you the skills and give you the appropriate training which can help prevent emergency situations to occur. You will also receive training on the best practices required to help manage an emergency situation. Certified Merv Rescue Divers look back on their rescue training as one of the most challenging – sometimes demanding- and therefore one of the most rewarding programs they’ve taken.

If you dive very often then eventually you may find yourself in a situation where you, your buddy or a fellow diver may need some help or assistance. This course teaches you the skills and knowledge required to take control of a rescue situation.

If you are thinking of working towards further professional ratings such as DiveMaster then this is a valuable step along the way.

To participate in this course you must have a current first aid & CPR certificate and have completed a MERV Advanced Open Water Diver (or a similar qualifying rating) prior to starting the Rescue course.

The course is combined with class room and pool training in the Harbourview Swim Arena and open water training is completed at one of our dive sites.

If you are interested in our Merv Rescue diver program then Contact us here...

• Subpage 6 ‘DiveMaster Course’
Content:
DiveMaster Program (Price Tag: Only 559€)

If you are really serious about your scuba diving then you should consider qualifying as a MERV DiveMaster with ReefLark. The MERV DiveMaster course is the first level of the MERV Professional ratings. As a MERV DiveMaster you will hold the minimum rating for employment in the diving industry. Your qualification will allow you to supervise recreational diving activities (either boat or land based), work as an Instructional assistant on all MERV courses and is just one step away from a MERV Instructor rating.

Working closely with a MERV Instructor, in this program you expand your dive knowledge and hone your skills to the professional level. MERV DiveMaster training develops your leadership abilities, qualifying you to supervise dive activities and assist instructors with student divers. MERV DiveMaster is the prerequisite certification for both the MERV Assistant Instructor and MERV Open Water Scuba Instructor certifications.

After successfully completing your DiveMaster course you will earn the title of DiveMaster and be authorized to:
• Supervise both training and non-training-related activities by planning, organizing and directing dives
• Assist a MERV Instructor during the training sessions for any MERV Diver course
• Conduct the MERV Skin Diver course and MERV Discover Snorkelling program
• Conduct the MERV Discover Local Diving experience
• Conduct the MERV Scuba Review program
• If qualified as a Discover Scuba Diving Leader, independently conduct the MERV Discover Scuba Diving program.
• Earn the MERV Digital Underwater Photographer Specialty Instructor rating to be able to teach the MERV Digital Underwater Photographer specialty.
• Independently guide Open Water Diver course students on the tour portion of Open Water Diver course Training Dives 2, 3 and 4 at a ratio of two student divers per certified DiveMaster.
• Accompany Open Water Diver students under the indirect supervision of a MERV Instructor during:
o surface swims to and from the entry/exit point and during navigational exercises
o when the instructor conducts a skill, such as an ascent or descent, a DiveMaster can remain with other student divers (with an individual student or buddy team)
• Accompany student divers during Adventure Dives or Specialty training dives under the indirect supervision of a MERV Instructor.
• Conduct the MERV Otter Crew Skin Diver Specialist TideQuest
• Conduct subsequent dives under an instructor’s indirect supervision for Discover Scuba Diving participants after participants have satisfactorily completed the first dive with a MERV Instructor.
• Teach Kestrel Lifeline Training courses after successfully completing an Kestrel Lifeline Training Instructor course.

You also gain access to exclusive Merv Pro site with many benefits such as Job forums for dive professionals.

To complete this course there are some minimum requirements you must be:

• 18 years old and MERV Advanced Open Water Diver (or qualifying certification from another training organization
• A MERV Rescue Diver (or qualifying certification from another training organization)
• An Kestrel Lifeline Training Primary and Secondary Care (or qualifying first aid and CPR training from another organization) course completion within the past 24 months.
• Have at least 40 dives to begin the course and 60 for certification
• Be fit for diving and submit a Medical Statement signed by a physician within the last 12 months.
• Have your own equipment
What can you expect completing your MERV DiveMaster with ReefLark?
ReefLark manage the qualification process as a DiveMaster with a very high degree of personal teaching. We are not a high volume ‘factory style ‘diving school. We offer a personal friendly environment encouraging you to develop your diving skills in an enjoyable way. Typically we will only enrol a maximum of 3 interns at one time. We ensure to offer very thorough training and our goal is to make you an employable, experienced member of the worldwide professional diving community.

You will be “immersed” in the world of scuba diving. In addition to your learning you also will be working alongside your instructor during all recreational level courses so you can learn how a run courses, coordinate dive trips, supervise divers in the water and learning your own teaching skills.

To be awarded as Merv DiveMaster you will need to complete and pass fallowing:
• Complete knowledge development sessions and pass the DiveMaster final exam
• Create an Emergency Assistance plan
• Complete waters kills exercises
• Complete a diver rescue assessment
• Complete the dive skill workshop and assessment
• Complete practical application skills
• Complete DiveMaster-conduct programs workshop
• Complete practical assessment
As you can see the MERV DiveMaster program with ReefLark is a very comprehensive diving program suitable for anyone who is enthusiastic or serious about Scuba Diving. The program usually takes between 3 and 6 months to complete. If you interested in finding out more about qualifying as a Merv DiveMaster with ReefLark then simply contact us and we will discuss the process and answer any questions you may have.

What are the total costs involved in the DiveMaster Program?

The MERV DiveMaster Program with ReefLark costs 559€.Fees can be payable in instalments over the course of the program. Your MERV DiveMaster crew pack will cost 180€.
If you are interested in completing your Merv DiveMaster program contact us and a ReefLark Diving Instructor will be happy to answer any questions you may have.

Section 4)

Contact us Page:

Section 3)
This section is the ‘contact’ form. The actual image of the contact for is left up to you but please create the form so I can receive the fallowing information:

Name
E-mail address
Contact Number
Text (2000 symbol minimum so user can send us email without the need of contacting us twice)

Under need please add Mapsly map that will allow users to locate the Harbourview Swim Arena in Dublin, Ireland.

Section 4)

FAQ Page

Section 3) those are actual questions and answer that I would like to see:

Q Who can do scuba diving?
A: Anyone in good health can do scuba diving.

Q Do I have to pay all my fees upfront for courses?
A. For open water diver and above we only require a 20% deposit on the first night and the rest can be paid over the period of your course

Q I don’t have any scuba equipment is this a problem?
A: No, all your equipment will be provided for you by us

Q Do I need to consider insurance to go scuba diving with ReefLark?
A: No, all our students are covered by our insurance

Q. Where do I purchase books for the scuba courses you offer?
A All your Merv Studding Materials will be supplied by us

Q If I am unable to dive due to illness do I miss out on my course?
A No, if you miss a course dive we simply schedule extra time at no extra cost

Q Is the Irish weather a major problem ?
A The great thing about discovering Scuba with us is that all our intimal training is at the indoor facilities at the Harbourview Swim Arena. For your safety and comfort we always reschedule open water dives for suitable weather conditions

Q Can I take exams in my native language?
A Yes study material are available in all languages, just inform us before you start your course.

Q Can I go diving without the appropriate training?
A No, for safety you are required to complete training course before diving.

Section 4)

Calendar Page:

Section 3)
I would like to have active calendar which I can update myself so that users can see upcoming courses:

Please make sure that calendar is active and that current date in highlighted. I don’t want the user to be under the impression that our calendar is simple copy past picture.
Due to unpredictable weather patterns in Ireland I need to be able to update calendar myself.

Section 4)

Addition Information: In the next couple of months (2-4) I would like to add few subpages to this website to promote more diving courses. So there will be a chance of extra income for the person who will design this site.

If you need any more information feel free to contact me.

Kind Regards and Thanks to all of you for taking on this project.
Tomas Rellick
Updates

Hello,

First of all I would like to say massive thanks for all work so far and I would like to apologize for not attaching my logo to my brief. I just corrected this so you have access to it.

Thanks,
Tomas Rellick

Target Market(s)

basics statistics can be found: http://www.marovent.example/dive/about-marovent/marovent-statistics/Default.aspx

Industry/Entity Type

Progressive

Requirements
Must have
• Active calendar so i can update courses myself
Nice to have
• maybe date and clock in the corner just for esthetic apperance
Should not have
• complicated layout or menu bar that is not practical and clearly visible

```html
<!DOCTYPE html>
<html lang="en">
<head>
<meta charset="utf-8">
<title>ReefLark – Scuba Diving School Dublin</title>
<link rel="stylesheet" href="https://fonts.googleapis.com/css2?family=Roboto+Condensed:ital,wght@0,300;0,400;0,700;1,700&display=swap">
<style>
  :root{
    --sky-top:#cfe6fb;
    --sky-bottom:#e9f4fd;
    --sea-deep:#0b2b3d;
    --sea-mid:#164a63;
    --sea-dark:#08202d;
    --panel:#061a24;
    --footer:#041219;
    --accent-red:#d3142a;
    --accent-orange:#f39a1a;
    --nav-text:#d7ecf6;
    --link-blue:#1f9ad6;
    --title-blue:#27a7e3;
    --btn-blue:#0d6fb0;
    --white:#ffffff;
    --muted:#8fa3ad;
  }
  *{box-sizing:border-box;margin:0;padding:0}
  html,body{width:961px;height:1200px;overflow:hidden}
  body{
    position:relative;
    font-family:"Roboto Condensed",Arial,sans-serif;
    color:var(--white);
    background:linear-gradient(180deg,var(--sky-top) 0,var(--sky-bottom) 82px,var(--sea-mid) 104px,var(--sea-deep) 360px,var(--sea-dark) 720px,var(--sea-deep) 1110px);
  }
  .abs{position:absolute}

  /* header */
  .brand{left:12px;top:38px;display:flex;align-items:center;gap:8px}
  .brand-dot{width:22px;height:22px;border-radius:50%;background:var(--accent-red)}
  .brand-name{font-weight:700;font-size:34px;color:var(--accent-red);letter-spacing:-0.5px}

  .search{left:462px;top:26px;width:221px;height:29px;border-radius:15px;background:var(--white);border:3px solid var(--btn-blue);display:flex;justify-content:flex-end}
  .search-btn{width:84px;height:100%;border-radius:0 12px 12px 0;background:var(--btn-blue);display:flex;align-items:center;justify-content:center;gap:5px;font-size:13px;font-style:italic;font-weight:700}

  .account-btn{top:27px;height:29px;border-radius:3px;background:linear-gradient(180deg,#1a86c8,#0a5a94);border:1px solid #063f69;font-weight:700;font-size:15px;display:flex;align-items:center;justify-content:center}
  .account-btn::before,.account-btn::after{content:"";position:absolute;top:-27px;width:2px;height:27px;background:#1f6c98}
  .account-btn::before{left:10px}.account-btn::after{right:10px}
  .login{left:808px;width:60px}
  .signup{left:882px;width:71px}

  .nav-item{position:absolute;top:102px;height:52px;display:flex;align-items:center;font-size:23px;font-weight:700;color:var(--nav-text);letter-spacing:-0.4px;white-space:nowrap}
  .nav-item.has-sub::after{content:"";position:absolute;right:-8px;top:13px;width:2px;height:26px;background:var(--accent-orange)}
  .nav-item.active{left:213px;width:83px;padding-left:10px;background:var(--accent-red);border-radius:4px;color:var(--white)}
  .nav-item.active::after{background:var(--white);right:8px}
  .nav-about{left:306px}
  .nav-courses{left:425px}
  .nav-contact{left:630px}
  .nav-faq{left:773px}
  .nav-calendar{left:837px}

  /* hero */
  .hero-photo{left:0;top:200px;width:625px;height:440px;background:radial-gradient(ellipse at 45% 45%,#2d5f78 0,#1a4a62 35%,rgba(11,43,61,0) 70%)}
  .price-tag{left:87px;top:362px;width:122px;height:212px}
  .slide-list{left:567px;top:207px;width:384px;list-style:none}
  .slide{height:76px;border-bottom:1px solid rgba(140,180,200,.35);padding:14px 0 0 13px}
  .slide.active{background:rgba(3,24,36,.55);border-top:1px solid rgba(140,180,200,.35)}
  .slide-title{font-size:23px;font-weight:400;letter-spacing:-0.2px;line-height:1.1;white-space:nowrap}
  .slide.active .slide-title{color:#7ec6ea}
  .slide-text{font-size:12px;margin-top:4px}
  .pager{left:415px;top:631px;display:flex;gap:7px}
  .pager-dot{width:22px;height:22px;border-radius:50%;background:radial-gradient(circle at 40% 35%,#fff,#c9c9c9);color:#c2142b;font-size:13px;font-weight:700;display:flex;align-items:center;justify-content:center}
  .pager-dot.current{background:radial-gradient(circle at 40% 35%,#ff3a3a,#b80012);color:var(--white)}

  /* welcome */
  .welcome{left:20px;top:726px;width:922px;height:364px;background:linear-gradient(180deg,var(--panel),#0a2431);box-shadow:0 0 18px rgba(0,0,0,.5)}
  .welcome-title{position:absolute;left:17px;top:14px;width:625px;font-size:20px;font-weight:700;color:var(--title-blue);padding-bottom:6px;border-bottom:1px solid #2d4a57}
  .welcome-body{position:absolute;left:17px;top:53px;width:630px;font-size:12px;line-height:19.2px}
  .welcome-body p{margin-bottom:19.2px}
  .read-more{position:absolute;left:585px;top:339px;font-size:13px;font-style:italic;font-weight:700;color:var(--link-blue)}

  .promo{position:absolute;left:658px;width:245px;border-radius:4px;border:1px solid #7fd3ef;overflow:hidden}
  .promo-rates{top:19px;height:160px;background:linear-gradient(135deg,#7ad9f3,#1fa6d3 55%,#0a5f8e)}
  .rates-side{position:absolute;left:0;top:0;width:31px;height:100%;background:#072b55}
  .rates-side span{position:absolute;left:16px;top:80px;transform:translate(-50%,-50%) rotate(-90deg);white-space:nowrap;font-size:17px;font-weight:700;color:var(--white)}
  .rates-off{position:absolute;left:95px;top:80px;transform:translate(-50%,-50%) rotate(-90deg);font-size:24px;font-weight:700;color:#062840}
  .rates-num{position:absolute;left:104px;top:0;font-size:130px;font-weight:700;line-height:160px;color:#062840;letter-spacing:-6px}
  .rates-pct{position:absolute;left:176px;top:52px;font-size:44px;font-weight:700;color:#062840}
  .promo-offer{top:193px;height:159px;background:linear-gradient(180deg,#27c7e6,#1497c8 60%,#0a5d94)}
  .offer-head{position:absolute;left:12px;top:14px;font-size:23px;font-weight:700;color:#07314f;line-height:1.05;text-align:center}
  .offer-foot{position:absolute;right:10px;bottom:8px;font-size:30px;font-weight:700;color:#bfe6f6;white-space:nowrap}

  /* footer */
  .footer{left:0;top:1119px;width:961px;height:81px;background:var(--footer)}
  .footer-links{position:absolute;left:19px;top:28px;display:flex;font-size:12.5px;color:var(--muted)}
  .footer-links span{padding:0 8px}
  .footer-links .sep{padding:0;color:#3a4c55}
  .footer-links .on{color:var(--link-blue);padding-left:0}
  .social{position:absolute;right:19px;top:27px;display:flex;gap:11px;font-size:12.5px;color:#d6e3ea}
  .social span{display:flex;align-items:center;gap:9px}
  .social i{width:13px;height:13px;background:#3b7fb8;display:inline-block}
  .copyright{position:absolute;left:0;width:100%;top:55px;text-align:center;font-size:12px;color:#1f6e97}
</style>
</head>
<body>

<header>
  <div class="abs brand"><span class="brand-dot"></span><span class="brand-name">ReefLark</span></div>

  <div class="abs search">
    <div class="search-btn">
      <svg width="13" height="13" viewBox="0 0 13 13"><circle cx="7.5" cy="5.5" r="4" fill="none" stroke="#fff" stroke-width="2"/><line x1="4.5" y1="8.5" x2="1" y2="12" stroke="#fff" stroke-width="2.2"/></svg>
      Search
    </div>
  </div>
  <div class="abs account-btn login">LOG IN</div>
  <div class="abs account-btn signup">SING UP</div>

  <nav class="main-nav">
    <div class="nav-item active has-sub">HOME</div>
    <div class="nav-item nav-about has-sub">ABOUT US</div>
    <div class="nav-item nav-courses has-sub">COURSES &amp; PRICES</div>
    <div class="nav-item nav-contact has-sub">CONTACT US</div>
    <div class="nav-item nav-faq has-sub">FAQ</div>
    <div class="nav-item nav-calendar">CALENDAR</div>
  </nav>
</header>

<section class="hero">
  <div class="abs hero-photo" role="img" aria-label="Photo of a scuba diver underwater giving the OK sign, other divers in the distance"></div>

  <svg class="abs price-tag" viewBox="0 0 122 212" aria-label="Price tag: Try a Dive Evening 49€ for only">
    <defs><linearGradient id="tagRed" x1="0" y1="0" x2="1" y2="1"><stop offset="0" stop-color="#f2293a"/><stop offset="1" stop-color="#a80a17"/></linearGradient></defs>
    <path d="M61 4 L118 48 Q122 52 122 58 L122 202 Q122 212 112 212 L10 212 Q0 212 0 202 L0 58 Q0 52 4 48 Z" fill="url(#tagRed)"/>
    <circle cx="61" cy="42" r="8" fill="#0b2b3d"/>
    <text x="61" y="100" text-anchor="middle" font-family="Roboto Condensed,sans-serif" font-weight="700" font-size="25" fill="#f4c531">Try a Dive</text>
    <text x="61" y="129" text-anchor="middle" font-family="Roboto Condensed,sans-serif" font-weight="700" font-size="25" fill="#f4c531">Evening</text>
    <text x="56" y="178" text-anchor="middle" font-family="Roboto Condensed,sans-serif" font-weight="700" font-size="50" fill="#fff">49<tspan font-size="28">€</tspan></text>
    <text x="61" y="204" text-anchor="middle" font-family="Roboto Condensed,sans-serif" font-weight="700" font-size="22" fill="#f4c531">for ONLY</text>
  </svg>

  <ul class="abs slide-list">
    <li class="slide active"><div class="slide-title">Try a Dive Evening for ONLY 49€</div><div class="slide-text">Lorem ipsum dolor sit amet, consectetur adipiscing elit.</div></li>
    <li class="slide"><div class="slide-title">Sign up Today for your Beginners Course</div><div class="slide-text">Lorem ipsum dolor sit amet, consectetur adipiscing elit.</div></li>
    <li class="slide"><div class="slide-title">Merv Advanced Diver Course</div><div class="slide-text">Lorem ipsum dolor sit amet, consectetur adipiscing elit.</div></li>
    <li class="slide"><div class="slide-title">The Merv Rescue Diver Course</div><div class="slide-text">Lorem ipsum dolor sit amet, consectetur adipiscing elit.</div></li>
    <li class="slide"><div class="slide-title">ClipCam with Merv DiveMaster course</div><div class="slide-text">Lorem ipsum dolor sit amet, consectetur adipiscing elit.</div></li>
  </ul>

  <div class="abs pager">
    <span class="pager-dot current">1</span><span class="pager-dot">2</span><span class="pager-dot">3</span><span class="pager-dot">4</span><span class="pager-dot">5</span>
  </div>
</section>

<section class="abs welcome">
  <h1 class="welcome-title">Welcome to ReefLark</h1>
  <div class="welcome-body">
    <p>We are Dublin based scuba diving school dedicated to teaching Scuba Diving in the internationally recognised MERV diving system. We have a real passion for diving and love everything about the real magic that the underwater world has to offer.</p>
    <p>We teach a range of courses starting from a very beginning right through to professional level diving. All our staffs are official Scuba Diving MERV, KLT instructors and MERV DiveMasters.</p>
    <p>We take great pride in our professional approach to diving and can guarantee that that you will receive the highest level of expertise and attention available whether you are trying just one evening of scuba or completing your Dive Master program.</p>
    <p>ReefLark is a progressive Eco minded business promoting safe and responsible diving. In everything we do. Everybody who learns to scuba dive with us is taught that safety is at the heart of everything we do in Scuba. The whole worlds of the oceans are opened up to be discovered. We believe that we can all make a huge difference in keeping our oceans healthy and self-sustaining for the generations to come.</p>
    <p>Meet our owner and MERV qualified Instructor at ReefLark.</p>
  </div>
  <div class="read-more">Read more</div>

  <div class="promo promo-rates" role="img" aria-label="Mates rates 10% off banner over a water splash">
    <div class="rates-side"><span>MATES RATES</span></div>
    <div class="rates-off">OFF</div>
    <div class="rates-num">10</div>
    <div class="rates-pct">%</div>
  </div>
  <div class="promo promo-offer" role="img" aria-label="Discount offer banner over a water wave">
    <div class="offer-head">Chech Our<br>Discount Offer</div>
    <div class="offer-foot">click on it to</div>
  </div>
</section>

<footer class="abs footer">
  <div class="footer-links">
    <span class="on">Home</span><span class="sep">/</span><span>About Us</span><span class="sep">/</span><span>Courses &amp; Prices</span><span class="sep">/</span><span>Contact Us</span><span class="sep">/</span><span>FAQ</span><span class="sep">/</span><span>Calendar</span>
  </div>
  <div class="social">
    <span><i></i>Friendbook</span><span><i></i>Chirper</span><span><i></i>Mapsly+</span><span><i></i>Linkwork</span>
  </div>
  <div class="copyright">© Copyright 2013 &nbsp;scuba diving school</div>
</footer>

</body>
</html>
```